Veltrano Energy Business Card Design

website: www.veltranoenergy.example
Project: Business Card Design for Veltrano Energy
Name: Dorian Kettle
Title: Founder / Operations Strategist
Visual Identity & Logo:
Logo File: VEL-Logo-FullGradient-Final.png (Attached).
Color Palette: The brand relies on a distinctive Cyan (Blue) to Lime Green gradient.
Background Preference: We want a Dark Mode aesthetic (Deep Matte Black, Charcoal, or Dark Slate) to make the neon gradient of the logo pop. This feels more "tech/industrial" than a standard white card.
Design Aesthetic (The "Ops" Vibe):
Concept: "Grid & Infrastructure." We are a solar rental company, focusing on logistics and access.
Typography: White, bold sans-serif text for contact info. High contrast against the dark background.
Accents: Use the Cyan or Lime Green from the logo for thin divider lines or edge painting.
Avoid: No orange/gold (clashes with logo). No cartoon leaves.
Layout Requirements:
Front: Large, centered logo. Maybe a subtle UV gloss spot varnish over the logo icon.
Back: Name, Title, Contact Info.
Texture: Matte finish cardstock with gloss elements.
sample mock up of information on card: https://brivomarkco-my.filehost.example/:i:/g/personal/dorian_kettle_veltranoenergy_example/AbCdEfGhIjKlMnOpQrStUvWxYz012345678?e=Xy12Ab
Logo: https://brivomarkco.filehost.example/:i:/s/VeltranoEnergy/ZyXwVuTsRqPoNmLkJiHgFeDcBa9876543210?e=Pq34Cd

```html
<!DOCTYPE html>
<html lang="en">
<head>
<meta charset="utf-8">
<title>Veltrano Energy Business Card</title>
<link rel="stylesheet" href="https://fonts.googleapis.com/css2?family=Montserrat:wght@500;600;800&family=Poppins:wght@400;500&display=swap">
<style>
  :root {
    --page: #d9d8d4;
    --card: #1f1f1f;
    --white: #ffffff;
    --cyan: #0aa6d8;
    --teal: #1fc8b4;
    --lime: #a6dc22;
    --flag-blue: #2b4a9b;
    --flag-red: #d0242c;
  }
  html, body {
    margin: 0;
    width: 1200px;
    height: 811px;
    overflow: hidden;
    background: var(--page);
  }
  .sheet {
    position: relative;
    width: 1200px;
    height: 811px;
  }
  .card {
    position: absolute;
    left: 280px;
    width: 640px;
    height: 366px;
    background: var(--card);
    overflow: hidden;
    box-shadow: 0 6px 18px rgba(0,0,0,0.18);
  }
  .card--back { top: 28px; }
  .card--front { top: 417px; }

  .edge-band {
    position: absolute;
    inset: 0;
  }
  .contact {
    position: absolute;
    left: 40px;
    top: 42px;
    color: var(--white);
    font-family: "Montserrat", sans-serif;
  }
  .contact__name {
    margin: 0;
    font-size: 30px;
    font-weight: 800;
    letter-spacing: 0.5px;
    background: linear-gradient(90deg, var(--cyan), var(--lime));
    -webkit-background-clip: text;
    background-clip: text;
    color: transparent;
  }
  .contact__title {
    margin: 6px 0 24px;
    font-size: 17px;
    font-weight: 500;
  }
  .contact__address {
    margin: 0 0 14px;
    font-size: 17px;
    font-weight: 500;
    line-height: 1.3;
    font-style: normal;
  }
  .contact__line {
    display: flex;
    align-items: center;
    gap: 8px;
    font-size: 17px;
    font-weight: 500;
    line-height: 1.4;
  }
  .contact__line svg { width: 15px; height: 15px; }
  .contact__slogan {
    margin: 16px 0 0;
    font-size: 17px;
    font-weight: 500;
  }

  .brand {
    position: absolute;
    display: flex;
    align-items: center;
    font-family: "Montserrat", sans-serif;
    font-weight: 600;
    color: var(--teal);
  }
  .brand__mark {
    background: var(--cyan);
  }
  .brand--small {
    right: 34px;
    top: 34px;
    gap: 10px;
    font-size: 26px;
  }
  .brand--small .brand__mark { width: 30px; height: 30px; }
  .tagline {
    position: absolute;
    font-family: "Poppins", sans-serif;
    color: var(--white);
    font-weight: 500;
  }
  .tagline--small {
    right: 36px;
    top: 76px;
    font-size: 9.5px;
  }

  .offices {
    position: absolute;
    right: 56px;
    top: 160px;
    display: flex;
    align-items: center;
    gap: 8px;
    font-family: "Poppins", sans-serif;
    font-size: 15px;
    color: var(--white);
  }
  .offices__flag {
    width: 30px;
    height: 30px;
    border-radius: 50%;
    border: 2px solid var(--white);
  }
  .offices__flag--us { background: linear-gradient(180deg, var(--flag-blue) 0 45%, var(--flag-red) 45%); }
  .offices__flag--ca { background: linear-gradient(90deg, var(--flag-red) 0 25%, var(--white) 25% 75%, var(--flag-red) 75%); }
  .offices__flag--uk { background: linear-gradient(135deg, var(--flag-blue), var(--flag-red), var(--flag-blue)); }

  .brand--large {
    left: 50%;
    top: 122px;
    transform: translateX(-50%);
    gap: 22px;
    font-size: 64px;
    white-space: nowrap;
  }
  .brand--large .brand__mark { width: 72px; height: 72px; }
  .tagline--large {
    left: 0;
    right: 0;
    top: 222px;
    text-align: center;
    font-size: 19px;
  }
</style>
</head>
<body>
<main class="sheet">

  <section class="card card--back" aria-label="Card back with contact details">
    <svg class="edge-band" viewBox="0 0 640 366" aria-hidden="true">
      <defs>
        <linearGradient id="bandGradient" x1="0" y1="1" x2="1" y2="0">
          <stop offset="0" stop-color="#0aa6d8"/>
          <stop offset="0.55" stop-color="#1fc8b4"/>
          <stop offset="1" stop-color="#a6dc22"/>
        </linearGradient>
      </defs>
      <polygon points="470,366 470,318 500,294 640,294 640,366" fill="url(#bandGradient)"/>
      <polyline points="240,340 450,340 462,330 462,306 494,282 640,282" fill="none" stroke="#0aa6d8" stroke-width="3"/>
      <rect x="240" y="348" width="230" height="18" fill="#a6dc22"/>
      <line x1="240" y1="345" x2="470" y2="345" stroke="#0aa6d8" stroke-width="3"/>
    </svg>

    <div class="brand brand--small">
      <span class="brand__mark"></span>
      <span class="brand__name">Veltrano Energy</span>
    </div>
    <p class="tagline tagline--small">Rent Solar. Generate Power. Save Smarter</p>

    <div class="offices">
      <span>Office</span>
      <span class="offices__flag offices__flag--us" role="img" aria-label="United States flag badge"></span>
      <span class="offices__flag offices__flag--ca" role="img" aria-label="Canada flag badge"></span>
      <span class="offices__flag offices__flag--uk" role="img" aria-label="United Kingdom flag badge"></span>
    </div>

    <div class="contact">
      <h1 class="contact__name">DORIAN KETTLE</h1>
      <p class="contact__title">Founder / Operations Strategist</p>
      <address class="contact__address">Veltrano Energy<br>4120 Harbor Crest Lane<br>Tampa, FL 33602</address>
      <div class="contact__line">
        <svg viewBox="0 0 16 16" aria-hidden="true"><path d="M3 1.5l3 .5 1 3.5-2 1.2a9 9 0 0 0 4.3 4.3l1.2-2 3.5 1 .5 3-2 1.5C6.5 14 2 9.5 1.5 3.5z" fill="#1fc8b4"/></svg>
        <span>555.014.2290</span>
      </div>
      <div class="contact__line">
        <svg viewBox="0 0 16 16" aria-hidden="true"><circle cx="8" cy="8" r="6.5" fill="none" stroke="#a6dc22" stroke-width="1.6"/><path d="M1.5 8h13M8 1.5c-3 3.5-3 9.5 0 13M8 1.5c3 3.5 3 9.5 0 13" fill="none" stroke="#0aa6d8" stroke-width="1.2"/></svg>
        <span>www.veltranoenergy.example</span>
      </div>
      <p class="contact__slogan">No debt, no liens, no maintenance, just savings.</p>
    </div>
  </section>

  <section class="card card--front" aria-label="Card front with brand name">
    <div class="brand brand--large">
      <span class="brand__mark"></span>
      <span class="brand__name">Veltrano Energy</span>
    </div>
    <p class="tagline tagline--large">Rent Solar. Generate Power. Save Smarter</p>
  </section>

</main>
</body>
</html>
```